CHRISTMAS CARD

We want a Christmas card for wealth managers to issue to high net worth clients. Very classy. Very corporate. The finished printed card will be a5 to fit existing envelopes. the design will also be used as part of a digital card so i need the image in a format for email as well as print. The brand uses a silver (foil block) on its logo and a specific pan tone ref olive green (reference 620). Not too religious and include a quirky message.

Target Market(s)

The target market is clients with investments. Typically more than £100,000 which is why the card needs to be very classy.

Industry/Entity Type

Religious

Requirements
Must have
• logo - but i can't work out how to attach it! i can email it tho. contact me on mira@tarvexlink.com

```html
<!DOCTYPE html>
<html lang="en">
<head>
<meta charset="utf-8">
<title>Seasons Greetings – Halden Group</title>
<link rel="stylesheet" href="https://fonts.googleapis.com/css2?family=Poiret+One&display=swap">
<style>
  :root {
    --slate-deep: #2f3530;
    --slate-mid: #414943;
    --slate-light: #4e5650;
    --snow: #ffffff;
    --snow-soft: rgba(255, 255, 255, 0.16);
    --type: #f2f3f0;
  }
  * { margin: 0; padding: 0; box-sizing: border-box; }
  html, body {
    width: 847px;
    height: 1200px;
    overflow: hidden;
  }
  .card {
    position: relative;
    width: 847px;
    height: 1200px;
    overflow: hidden;
    background:
      radial-gradient(ellipse 520px 420px at 620px 700px, rgba(255,255,255,0.05), transparent 70%),
      radial-gradient(ellipse 600px 500px at 200px 250px, rgba(255,255,255,0.04), transparent 70%),
      linear-gradient(160deg, var(--slate-light) 0%, var(--slate-mid) 45%, var(--slate-deep) 100%);
    font-family: "Poiret One", sans-serif;
    color: var(--type);
  }
  .snowflake-wreath {
    position: absolute;
    left: -120px;
    top: -60px;
    width: 966px;
    height: 1000px;
    background: radial-gradient(circle at 483px 462px,
      transparent 0 300px,
      var(--snow-soft) 340px 420px,
      transparent 470px);
  }
  .greeting {
    position: absolute;
    left: 0;
    top: 352px;
    width: 690px;
    text-align: center;
    font-weight: 400;
    line-height: 1;
  }
  .greeting__main {
    display: block;
    font-size: 62px;
    letter-spacing: 1px;
  }
  .greeting__sub {
    display: block;
    margin-top: 10px;
    font-size: 50px;
  }
  .brand {
    position: absolute;
    left: 303px;
    top: 1070px;
    width: 290px;
    text-align: center;
    font-size: 34px;
    letter-spacing: 8px;
    color: var(--type);
    line-height: 1;
  }
</style>
</head>
<body>
  <main class="card">
    <div class="snowflake-wreath" role="img" aria-label="Wreath of white stylised snowflakes circling the greeting"></div>
    <h1 class="greeting">
      <span class="greeting__main">Seasons Greetings</span>
      <span class="greeting__sub">from us all</span>
    </h1>
    <div class="brand">HALDEN GROUP</div>
  </main>
</body>
</html>
```